Tolvern Business Cards

Business card design. dont mind if new logo is suggested.
it would be for a security company.
our clients would be bigger security companies around Australia.
have a logo done but can be replaced. see attaached. like the colors.
Need company name, person name, designation, phone and email on front.
At back company logo and name. website saddress and 2 x license numbers
would like to have 2 different background color for both sidde

Industry/Entity Type

Security

Contact Information for Business Card

round corners, front should be light in color. need logo at back with webaddress and 2 x license numners

Font styles to use
Sans Serif

Colors
f37122
faa54b
f8ba93
0255a3
0592cd
85cae6
b3d448
9bcb3c
ffffff

Requirements
Must have
• see description
Nice to have
• see description
Should not have
• should not be difficult to read or hardd to find information on card.. lets say easy on eyes yet catchy

```html
<!DOCTYPE html>
<html lang="en">
<head>
<meta charset="utf-8">
<title>Tolvern Security Group – Business Cards</title>
<link rel="stylesheet" href="https://fonts.googleapis.com/css2?family=Cinzel:wght@400;600&family=Crimson+Text:wght@400&display=swap">
<style>
  :root {
    --stage: #ece7df;
    --card-white: #ffffff;
    --navy: #1d3f8a;
    --ink-grey: #6f7480;
    --rule-blue: #4a6fb0;
    --blue-deep: #0a3c7c;
    --blue-mid: #0c62a6;
    --blue-glow: #19a9d2;
    --dot-soft: #d7e6ef;
    --dot-deep: rgba(8, 48, 110, 0.55);
    --white: #ffffff;
  }
  * { box-sizing: border-box; margin: 0; padding: 0; }
  html, body {
    width: 1200px; height: 802px; overflow: hidden;
    background: var(--stage);
  }
  .stage {
    position: relative; width: 1200px; height: 802px;
  }
  .card {
    position: absolute;
    width: 540px; height: 309px;
    border-radius: 26px;
    overflow: hidden;
    box-shadow: 0 6px 18px rgba(0,0,0,0.18);
  }
  /* Front card */
  .card--front {
    left: 40px; top: 246px;
    background: var(--card-white);
  }
  .front__texture {
    position: absolute; right: 0; top: 0;
    width: 270px; height: 230px;
    background: radial-gradient(ellipse at 65% 40%, var(--dot-soft) 0%, rgba(215,230,239,0.4) 45%, rgba(255,255,255,0) 75%);
  }
  .brand {
    position: absolute; left: 40px; top: 62px;
    display: flex; align-items: center; gap: 12px;
  }
  .brand__mark {
    width: 34px; height: 34px; border-radius: 50%;
    background: var(--navy);
  }
  .brand__name {
    font-family: "Cinzel", serif; font-weight: 600;
    font-size: 17px; letter-spacing: 0.5px;
    color: var(--navy);
  }
  .front__rule {
    position: absolute; left: 300px; top: 132px;
    width: 200px; height: 1px; background: var(--rule-blue);
  }
  .person {
    position: absolute; left: 40px; top: 190px;
  }
  .person__line {
    display: flex; align-items: baseline; gap: 8px;
  }
  .person__name {
    font-family: "Cinzel", serif; font-weight: 600;
    font-size: 24px; color: var(--navy); letter-spacing: 0.5px;
  }
  .person__role {
    font-family: "Crimson Text", serif; font-size: 14px;
    color: var(--ink-grey);
  }
  .person__contact, .address {
    font-family: "Crimson Text", serif; font-size: 13.5px;
    line-height: 1.35; color: var(--ink-grey);
  }
  .person__contact { margin-top: 6px; }
  .address {
    position: absolute; left: 300px; top: 150px;
  }
  /* Back card */
  .card--back {
    left: 620px; top: 246px;
    background: radial-gradient(ellipse at 42% 52%, var(--blue-glow) 0%, var(--blue-mid) 38%, var(--blue-deep) 85%);
  }
  .back__texture {
    position: absolute; right: 0; top: 0;
    width: 260px; height: 260px;
    background: radial-gradient(ellipse at 70% 35%, var(--dot-deep) 0%, rgba(8,48,110,0.15) 50%, rgba(8,48,110,0) 75%);
  }
  .back__brand {
    position: absolute; left: 0; right: 0; top: 110px;
    text-align: center;
    font-family: "Cinzel", serif; font-weight: 600;
    font-size: 27px; letter-spacing: 1px; color: var(--white);
  }
  .back__web {
    position: absolute; left: 0; right: 0; top: 176px;
    text-align: center;
    font-family: "Crimson Text", serif; font-size: 15px;
    color: var(--white); letter-spacing: 0.5px;
  }
  .back__rule {
    position: absolute; left: 110px; right: 70px; top: 202px;
    height: 1px; background: rgba(255,255,255,0.75);
  }
  .back__licenses {
    position: absolute; left: 0; right: 0; top: 210px;
    text-align: center;
    font-family: "Crimson Text", serif; font-size: 15px;
    color: var(--white); letter-spacing: 0.5px;
  }
</style>
</head>
<body>
<main class="stage">
  <section class="card card--front" aria-label="Business card front">
    <div class="front__texture" role="img" aria-label="Soft pale blue dotted texture"></div>
    <div class="brand">
      <span class="brand__mark"></span>
      <span class="brand__name">TOLVERN SECURITY GROUP</span>
    </div>
    <div class="front__rule"></div>
    <div class="address">
      <p>Dummy Street</p>
      <p>Dummy City, Dummy Country</p>
    </div>
    <div class="person">
      <p class="person__line">
        <span class="person__name">JOHN DOE</span>
        <span class="person__role">| Director</span>
      </p>
      <div class="person__contact">
        <p>+63 900 555 0147</p>
        <p>john@tolvern.com</p>
      </div>
    </div>
  </section>

  <section class="card card--back" aria-label="Business card back">
    <div class="back__texture" role="img" aria-label="Faint deep blue dotted texture"></div>
    <h1 class="back__brand">TOLVERN SECURITY GROUP</h1>
    <p class="back__web">www.tolvern.com</p>
    <div class="back__rule"></div>
    <p class="back__licenses">license no: XXXX XX | license no: XXXX XX</p>
  </section>
</main>
</body>
</html>
```